Amber Lantern Cafe Business Card

We need a business card design for a new European Cafe. Main menu will be coffee and deserts.

Requirements
Must have
• Logo - 1 of the attached versions
Address - TBA (you can use 487 Morrow Ave Unit 9 for now)
Phone - TBA (you can use 555-238-4176 for now)

```html
<!DOCTYPE html>
<html lang="en">
<head>
<meta charset="utf-8">
<title>Amber Lantern Cafe – Business Card</title>
<link rel="stylesheet" href="https://fonts.googleapis.com/css2?family=Mulish:wght@600;800&display=swap">
<style>
  :root {
    --backdrop: #efe9e1;
    --burlap: #c9b497;
    --burlap-light: #d6c4aa;
    --espresso: #3a2218;
    --pocket: #5a3d2b;
    --pocket-edge: #3f281b;
    --pocket-trim: #c7b59c;
    --bean-dark: #4a2c18;
    --bean-mid: #7a4c2a;
    --ink: #2b1a12;
    --cream: #ffffff;
  }
  * { margin: 0; padding: 0; box-sizing: border-box; }
  html, body { width: 1200px; height: 1000px; overflow: hidden; }
  body {
    background: var(--backdrop);
    font-family: "Mulish", "Century Gothic", sans-serif;
    position: relative;
  }
  .business-card {
    position: absolute;
    left: 100px;
    top: 220px;
    width: 1000px;
    height: 560px;
    background: radial-gradient(ellipse at 60% 40%, var(--burlap-light), var(--burlap));
    overflow: hidden;
    box-shadow: 0 10px 30px rgba(0,0,0,0.18);
  }
  .bean-band {
    position: absolute;
    left: 0;
    bottom: 0;
    width: 100%;
    height: 230px;
    background: linear-gradient(to bottom,
      rgba(122,76,42,0) 0%,
      rgba(122,76,42,0.55) 22%,
      var(--bean-mid) 45%,
      var(--bean-dark) 100%);
  }
  .pocket {
    position: absolute;
    left: 80px;
    top: 0;
    width: 360px;
    height: 370px;
  }
  .pocket-name {
    position: absolute;
    left: 80px;
    top: 120px;
    width: 340px;
    text-align: center;
    color: var(--cream);
    font-weight: 800;
    font-size: 40px;
    line-height: 1.15;
  }
  .brand {
    position: absolute;
    left: 540px;
    top: 40px;
    width: 420px;
    text-align: center;
    color: var(--ink);
  }
  .brand-mark {
    display: block;
    width: 150px;
    height: 125px;
    margin: 0 auto 28px;
    background: var(--espresso);
  }
  .brand-name {
    font-weight: 800;
    font-size: 44px;
    line-height: 1.1;
  }
  .contact {
    margin-top: 36px;
    font-weight: 800;
    font-size: 29px;
    line-height: 1.35;
  }
</style>
</head>
<body>
  <article class="business-card">
    <div class="bean-band" role="img" aria-label="Roasted coffee beans scattered across the burlap along the bottom of the card"></div>

    <svg class="pocket" viewBox="0 0 360 370" aria-hidden="true">
      <path d="M10 0 V250 Q10 360 120 360 H260 Q350 360 350 250 V0 Z" fill="var(--pocket-edge)"/>
      <path d="M0 0 V240 Q0 350 110 350 H240 Q330 350 330 240 V0 Z" fill="var(--pocket)" stroke="var(--pocket-trim)" stroke-width="5"/>
    </svg>
    <p class="pocket-name">Amber<br>Lantern<br>Cafe</p>

    <div class="brand">
      <span class="brand-mark" aria-hidden="true"></span>
      <h1 class="brand-name">Amber Lantern Cafe</h1>
      <p class="contact">
        487 Morrow Ave Unit 9<br>
        Phone: 555-238-4176
      </p>
    </div>
  </article>
</body>
</html>
```